Create a business promotion flyer to leave in customer mailboxes. We are a bulk petroleum supplier, servicing any industry that requires diesel. Base in griffith NSW, servicing griffith area and surrounds.

Business Name - Terra Petro
Fuel@terrapetro-example.com.au
Marco - 0400 000 001 mtorrisi@terrapetro-example.com.au
Liam - 0400 000 002 lharcourt@terrapetro-example.com.au
Peter - 0400 000 003 pwinslow@terrapetro-example.com.au
Office 02 5550 0100

Bulk Fuel deliveries.
Oils & lubricants
Local Family owned business

```html
<!DOCTYPE html>
<html lang="en">
<head>
<meta charset="utf-8">
<title>Terra Petro – Bulk Fuel Deliveries Flyer</title>
<link rel="stylesheet" href="https://fonts.googleapis.com/css2?family=Montserrat:wght@400;500;600;700;800&display=swap">
<style>
  :root {
    --brand-red: #e2231a;
    --brand-red-deep: #c41912;
    --steel-grey: #56585b;
    --steel-light: #8a8c8f;
    --ink: #222325;
    --paper: #ffffff;
    --backdrop: #b3b3b3;
    --card-shadow: rgba(0, 0, 0, 0.16);
  }
  * { box-sizing: border-box; margin: 0; padding: 0; }
  html, body {
    width: 1200px; height: 1200px; overflow: hidden;
    background: var(--backdrop);
    font-family: "Montserrat", Arial, sans-serif;
    color: var(--ink);
  }
  .flyer {
    position: absolute; left: 192px; top: 30px;
    width: 816px; height: 1140px;
    background: var(--paper);
    overflow: hidden;
  }
  .brand {
    position: absolute; top: 62px; left: 0; width: 100%;
    display: flex; justify-content: center; align-items: center; gap: 10px;
  }
  .brand-mark { width: 16px; height: 16px; background: var(--brand-red); }
  .brand-name {
    font-size: 34px; font-weight: 600; color: var(--brand-red); letter-spacing: 0.2px;
  }
  .headline {
    position: absolute; top: 138px; left: 0; width: 100%;
    text-align: center; font-size: 41px; font-weight: 700; line-height: 49px;
    color: var(--ink);
  }
  .hero {
    position: absolute; top: 253px; left: 0; width: 816px; height: 420px;
  }
  .hero svg { position: absolute; inset: 0; }
  .hero-truck {
    position: absolute; left: 22px; top: 108px; width: 782px; height: 186px;
    border-radius: 14px 40px 10px 10px;
    background: linear-gradient(180deg, #ffffff 0%, #eceae6 55%, #9c9d9f 100%);
  }
  .intro {
    position: absolute; top: 672px; left: 60px; width: 696px;
    text-align: center; font-size: 19px; font-weight: 500; line-height: 25px;
  }
  .intro strong { font-weight: 700; }
  .services {
    position: absolute; top: 768px; left: 45px; width: 728px;
    display: grid; grid-template-columns: repeat(3, 1fr); gap: 22px;
  }
  .service-card {
    height: 186px; background: var(--paper);
    box-shadow: 0 4px 12px var(--card-shadow);
    display: flex; flex-direction: column; align-items: center; justify-content: flex-start;
    padding-top: 22px;
  }
  .service-card svg { width: 72px; height: 72px; }
  .service-title {
    margin-top: 16px; text-align: center;
    font-size: 21px; font-weight: 600; line-height: 26px;
  }
  .contact-heading {
    position: absolute; top: 994px; left: 45px;
    font-size: 27px; font-weight: 700;
  }
  .contacts {
    position: absolute; top: 1036px; left: 45px; width: 736px;
    display: grid; grid-template-columns: 175px 185px 195px 181px;
  }
  .contact { display: grid; grid-template-columns: 24px 1fr; row-gap: 2px; }
  .contact .icon { width: 18px; height: 18px; align-self: center; }
  .contact-name { font-size: 18px; font-weight: 600; }
  .contact-phone { grid-column: 2; font-size: 17px; font-weight: 600; }
  .contact-email { grid-column: 2; font-size: 12px; font-weight: 500; line-height: 15px; margin-top: 2px; }
  .contact-email.with-icon { grid-column: 1 / 3; display: grid; grid-template-columns: 24px 1fr; }
</style>
</head>
<body>
  <main class="flyer">
    <header class="brand">
      <span class="brand-mark"></span>
      <span class="brand-name">Terra Petro</span>
    </header>

    <h1 class="headline">Powering Your Business with<br>Reliable Bulk Fuel Deliveries</h1>

    <section class="hero">
      <svg viewBox="0 0 816 420" width="816" height="420" aria-hidden="true">
        <path d="M0 58 C200 28 420 92 816 18 L816 112 C520 150 260 92 0 150 Z" fill="var(--steel-grey)"/>
        <path d="M0 18 C220 62 430 70 816 0 L816 40 C470 118 240 108 0 72 Z" fill="var(--brand-red)"/>
        <path d="M0 150 C250 118 520 168 816 118 L816 262 C520 300 250 268 0 300 Z" fill="var(--brand-red)"/>
        <path d="M0 240 C240 300 520 280 816 232 L816 300 C520 340 260 330 0 330 Z" fill="var(--steel-grey)"/>
        <path d="M0 300 C260 350 520 320 816 262 L816 336 C520 372 260 384 0 372 Z" fill="var(--brand-red-deep)"/>
        <path d="M0 378 C300 396 560 362 816 318 L816 360 C560 410 300 420 0 420 Z" fill="var(--steel-grey)"/>
        <path d="M0 330 C250 352 520 336 816 290 L816 300 C520 344 250 362 0 342 Z" fill="var(--paper)"/>
      </svg>
      <div class="hero-truck" role="img" aria-label="Photograph of a white road-train fuel tanker truck with red striped tanks"></div>
    </section>

    <p class="intro"><strong>Terra Petro</strong> is your trusted local family-owned bulk diesel supplier, proudly servicing Griffith and all surrounding areas with efficient, dependable service.</p>

    <section class="services">
      <article class="service-card">
        <svg viewBox="0 0 72 72" fill="none" stroke="var(--ink)" stroke-width="2.4" stroke-linecap="round" stroke-linejoin="round" aria-hidden="true">
          <path d="M20 62 L30 40 L44 46 L38 62 Z"/>
          <path d="M30 40 L36 26 L50 32 L44 46"/>
          <path d="M43 29 L52 16 C56 12 62 14 62 20"/>
          <path d="M62 30 C60 34 60 36 62 37 C64 36 64 34 62 30 Z"/>
        </svg>
        <h2 class="service-title">Bulk Fuel<br>Deliveries</h2>
      </article>
      <article class="service-card">
        <svg viewBox="0 0 72 72" fill="none" stroke="var(--ink)" stroke-width="2.4" stroke-linecap="round" stroke-linejoin="round" aria-hidden="true">
          <rect x="10" y="12" width="32" height="48" rx="3"/>
          <line x1="10" y1="22" x2="42" y2="22"/>
          <line x1="10" y1="50" x2="42" y2="50"/>
          <line x1="16" y1="8" x2="24" y2="8"/>
          <path d="M26 29 C22 35 22 39 26 40 C30 39 30 35 26 29 Z"/>
          <circle cx="52" cy="50" r="6"/>
          <path d="M52 38 V42 M52 58 V62 M40 50 H44 M60 50 H64 M44 42 L47 45 M57 55 L60 58 M44 58 L47 55 M57 45 L60 42"/>
        </svg>
        <h2 class="service-title">Oils &amp;<br>Lubricants</h2>
      </article>
      <article class="service-card">
        <svg viewBox="0 0 72 72" fill="none" stroke="var(--ink)" stroke-width="2.4" stroke-linecap="round" stroke-linejoin="round" aria-hidden="true">
          <path d="M20 30 L36 14 L52 30"/>
          <path d="M24 26 V40 M48 26 V40"/>
          <rect x="32" y="26" width="8" height="8"/>
          <path d="M8 46 L20 40 L34 50 C36 52 34 56 30 54 L24 50"/>
          <path d="M64 46 L52 40 L38 50 L46 58 C48 60 52 58 50 55"/>
          <path d="M30 54 L36 60 C38 62 42 60 40 57"/>
        </svg>
        <h2 class="service-title">Local Family<br>Owned Business</h2>
      </article>
    </section>

    <h2 class="contact-heading">Contact Our Team Today</h2>

    <section class="contacts">
      <div class="contact">
        <svg class="icon" viewBox="0 0 20 20" aria-hidden="true"><path d="M4 2 L8 2 L9 6 L7 8 C8 11 9 12 12 13 L14 11 L18 12 L18 16 C18 17 17 18 16 18 C8 18 2 12 2 4 C2 3 3 2 4 2 Z" fill="var(--brand-red)"/></svg>
        <span class="contact-name">Office</span>
        <span class="contact-phone">02 5550 0100</span>
        <span class="contact-email with-icon">
          <svg class="icon" viewBox="0 0 20 20" aria-hidden="true"><rect x="2" y="4" width="16" height="12" fill="none" stroke="var(--brand-red)" stroke-width="2"/><path d="M2 4 L10 11 L18 4" fill="none" stroke="var(--brand-red)" stroke-width="2"/></svg>
          <span>Fuel@<wbr>terrapetro-example.com.au</span>
        </span>
      </div>
      <div class="contact">
        <svg class="icon" viewBox="0 0 20 20" aria-hidden="true"><path d="M4 2 L8 2 L9 6 L7 8 C8 11 9 12 12 13 L14 11 L18 12 L18 16 C18 17 17 18 16 18 C8 18 2 12 2 4 C2 3 3 2 4 2 Z" fill="var(--brand-red)"/></svg>
        <span class="contact-name">Marco</span>
        <span class="contact-phone">0400 000 001</span>
        <span class="contact-email">mtorrisi@<wbr>terrapetro-example.com.au</span>
      </div>
      <div class="contact">
        <svg class="icon" viewBox="0 0 20 20" aria-hidden="true"><path d="M10 1 C6 1 3 4 3 8 C3 13 10 19 10 19 C10 19 17 13 17 8 C17 4 14 1 10 1 Z M10 5 A3 3 0 1 1 10 11 A3 3 0 1 1 10 5 Z" fill="var(--brand-red)" fill-rule="evenodd"/></svg>
        <span class="contact-name">Liam</span>
        <span class="contact-phone">0400 000 002</span>
        <span class="contact-email">lharcourt@<wbr>terrapetro-example.com.au</span>
      </div>
      <div class="contact">
        <span></span>
        <span class="contact-name">Peter</span>
        <span class="contact-phone">0400 000 003</span>
        <span class="contact-email">pwinslow@<wbr>terrapetro-example.com.au</span>
      </div>
    </section>
  </main>
</body>
</html>
```